" A empresa está localizada numa cidade pequena, porém muito próximos da capital do estado de Minas Gerais e de outras cidades maiores do interior. Considerada região metropolitana da capital. Criaremos um site e faremos venda de produtos na loja virtual, bem como marcação de serviços. Queremos trazer profissionalismo e um serviço diferenciado para a região. Nossa meta é em 3 anos ser a principal referência nesse serviço num raio de 50 km da cidade. "

```html
<!DOCTYPE html>
<html lang="pt-BR">
<head>
<meta charset="UTF-8">
<title>Vila Sálvia — Cartão Fidelidade</title>
<link href="https://fonts.googleapis.com/css2?family=Cormorant+Garamond:wght@500;600&family=Montserrat:wght@500;600&display=swap" rel="stylesheet">
<style>
  :root {
    --bg: #ececec;
    --card-dark: #0d3536;
    --card-mid: #1b5556;
    --gold: #c9a96a;
    --gold-soft: #b8975a;
    --ink-light: #eef2f1;
  }
  * { margin: 0; padding: 0; box-sizing: border-box; }
  html, body { width: 1200px; height: 1200px; overflow: hidden; }
  body {
    background: var(--bg);
    font-family: "Montserrat", sans-serif;
    position: relative;
  }
  .card {
    position: absolute;
    left: 220px;
    width: 760px;
    height: 410px;
    border-radius: 26px;
    background: radial-gradient(ellipse at 45% 40%, var(--card-mid) 0%, var(--card-dark) 75%);
    overflow: hidden;
  }
  .card--front { top: 170px; }
  .card--back { top: 640px; }

  .brand {
    position: absolute;
    text-align: center;
    font-family: "Cormorant Garamond", serif;
  }
  .brand__name {
    color: var(--gold);
    font-weight: 600;
    letter-spacing: 1px;
    line-height: 1;
    white-space: nowrap;
  }
  .brand__mark {
    display: block;
    margin: 0 auto;
    border-radius: 50%;
    background: var(--gold);
  }
  .brand__tagline {
    color: var(--gold-soft);
    text-transform: uppercase;
    font-weight: 500;
    letter-spacing: 1px;
    white-space: nowrap;
  }
  .card--front .brand { left: 100px; top: 85px; width: 560px; }
  .card--front .brand__mark { width: 70px; height: 70px; margin-bottom: 28px; }
  .card--front .brand__name { font-size: 64px; }
  .card--front .brand__tagline { font-size: 22px; margin-top: 4px; }
  .front-label {
    position: absolute;
    left: 100px; width: 560px;
    top: 345px;
    text-align: center;
    color: var(--gold);
    font-weight: 600;
    font-size: 22px;
    letter-spacing: 5px;
  }

  .card--back .brand { left: 40px; top: 42px; width: 300px; }
  .card--back .brand__mark { width: 44px; height: 44px; margin-bottom: 20px; }
  .card--back .brand__name { font-size: 40px; }
  .card--back .brand__tagline { font-size: 14px; margin-top: 2px; }

  .contact {
    position: absolute;
    left: 48px;
    color: var(--ink-light);
    font-size: 19px;
    font-weight: 500;
    display: flex;
    align-items: flex-start;
    gap: 12px;
    line-height: 1.3;
  }
  .contact svg { flex: none; width: 26px; height: 26px; }
  .contact--phone { top: 268px; align-items: center; }
  .contact--address { top: 322px; }

  .stamps {
    position: absolute;
    left: 440px; top: 40px;
    display: grid;
    grid-template-columns: 124px 124px;
    gap: 12px;
  }
  .stamp {
    width: 124px; height: 124px;
    border: 2px solid var(--gold);
    border-radius: 10px;
  }
</style>
</head>
<body>

  <section class="card card--front">
    <div class="brand">
      <span class="brand__mark"></span>
      <div class="brand__name">VILA SÁLVIA</div>
      <div class="brand__tagline">Cuidado que te valoriza</div>
    </div>
    <div class="front-label">CARTÃO FIDELIDADE</div>
  </section>

  <section class="card card--back">
    <div class="brand">
      <span class="brand__mark"></span>
      <div class="brand__name">VILA SÁLVIA</div>
      <div class="brand__tagline">Cuidado que te valoriza</div>
    </div>

    <div class="contact contact--phone">
      <svg viewBox="0 0 24 24" aria-hidden="true">
        <circle cx="12" cy="12" r="12" fill="#c9a96a"/>
        <path d="M8.3 6.5c.4-.3 1-.2 1.2.3l1 2c.2.4.1.8-.2 1.1l-.7.6c.6 1.3 1.6 2.4 2.9 3l.6-.7c.3-.3.8-.4 1.1-.2l2 1c.5.2.6.8.3 1.2l-.8 1c-.5.6-1.3.8-2 .5-3-1.2-5.3-3.5-6.5-6.5-.3-.7-.1-1.5.5-2z" fill="#0d3536"/>
      </svg>
      <span>(31) 9 9482-1036</span>
    </div>

    <div class="contact contact--address">
      <svg viewBox="0 0 24 24" aria-hidden="true">
        <path d="M12 1.5c-4.4 0-8 3.4-8 7.7 0 5.6 8 13.3 8 13.3s8-7.7 8-13.3c0-4.3-3.6-7.7-8-7.7z" fill="#c9a96a"/>
        <circle cx="12" cy="9.2" r="3.2" fill="#0d3536"/>
      </svg>
      <span>Rua das Acácias, 148<br>Vale Verde - MG</span>
    </div>

    <div class="stamps">
      <div class="stamp"></div>
      <div class="stamp"></div>
      <div class="stamp"></div>
      <div class="stamp"></div>
    </div>
  </section>

</body>
</html>
```